Construction Company business card and Logo.

We need a business card for a Building Company.
We build and constuction manage.
A simple logo is also required. Ive attached some samples that may assist.
Logo colours: Blue,sunburnt orange,lime/green and brown/grey.
The Font for the Brenvale logo ive been using is Georgia.
Maybe the A in Brenvale can be like my logo design..?
All other font either calibri or arial, something simple.
Simple/modern and neat is what i am looking for.
My card should look organised to convey what the company is about.

Target Market(s)

Developers, architects, proffesionals in general

Industry/Entity Type

Business

Contact Information for Business Card

Brenvale Constructions Pty Ltd
ACN: 381 607 912 Lic:617382D
Derek Lomavich
Managing Director
0438 215 706
derek@brenvale.com.au
www.brenvale.com.au
Industrial.Commercial.Residential.Build Management

Requirements
Must have
• Ive attached some ideas for the logo. Its simple. If you come up with something else, please show me as im not 100% sure of what i want.
The front of the card should be white.
The back of the card should have the company name and logo with Blue background
Should not have
• the design should be simple.
No old style fonts or italics etc

```html
<!DOCTYPE html>
<html lang="en">
<head>
<meta charset="utf-8">
<title>Brenvale Constructions – Business Card</title>
<link rel="stylesheet" href="https://fonts.googleapis.com/css2?family=Open+Sans:wght@400;600;700&display=swap">
<style>
  :root {
    --backdrop: #e6e7ea;
    --card-white: #f4f6f9;
    --charcoal: #48494b;
    --charcoal-light: #5b5c5f;
    --charcoal-dark: #3f4042;
    --text-dark: #4a4b4d;
    --text-mid: #606164;
    --text-soft: #9a9ca0;
    --brand-blue: #1669a0;
    --band-text: #dfe1e4;
  }
  * { box-sizing: border-box; margin: 0; padding: 0; }
  html, body { width: 1200px; height: 903px; overflow: hidden; }
  body {
    background: var(--backdrop);
    font-family: "Open Sans", Arial, sans-serif;
    position: relative;
  }
  .card {
    position: absolute;
    top: 300px;
    width: 500px;
    height: 305px;
    overflow: hidden;
    box-shadow: 0 6px 18px rgba(0,0,0,0.12);
  }
  /* Back of card */
  .card-back { left: 70px; background: var(--charcoal); }
  .card-back .facets { position: absolute; inset: 0; }
  .card-back .wordmark {
    position: absolute; left: 150px; top: 112px;
    color: #ffffff;
  }
  /* Front of card */
  .card-front { left: 630px; background: var(--card-white); }
  .card-front .wordmark {
    position: absolute; left: 40px; top: 62px;
    color: var(--text-dark);
  }
  .wordmark .mark-square {
    display: inline-block; width: 14px; height: 14px;
    background: currentColor; margin-right: 10px; vertical-align: 4px;
  }
  .wordmark .name {
    font-size: 40px; font-weight: 600; letter-spacing: -0.5px; line-height: 1;
  }
  .wordmark .legal {
    display: block; font-size: 15px; font-weight: 600; margin-top: 4px; padding-left: 24px;
  }
  .contact {
    position: absolute; left: 300px; top: 92px;
    color: var(--text-dark);
  }
  .contact .person { font-size: 15px; font-weight: 700; text-transform: uppercase; letter-spacing: 0.3px; }
  .contact .role { font-size: 11.5px; color: var(--text-mid); margin: 2px 0 0 14px; }
  .contact .lines { margin: 18px 0 0 40px; font-size: 11.5px; line-height: 1.45; color: var(--text-mid); }
  .contact .lines b { color: var(--text-dark); font-weight: 700; }
  .web {
    position: absolute; left: 150px; top: 208px;
    font-size: 13px; color: var(--text-dark);
  }
  .web .domain { color: var(--brand-blue); font-weight: 700; }
  .registration {
    position: absolute; left: 162px; top: 228px;
    font-size: 8.5px; color: var(--text-soft); letter-spacing: 0.2px;
  }
  .services {
    position: absolute; left: 0; right: 0; bottom: 0; height: 40px;
    background: var(--charcoal);
    color: var(--band-text);
    font-size: 16px; letter-spacing: 0.3px;
    display: flex; align-items: center; justify-content: center;
  }
</style>
</head>
<body>
  <section class="card card-back" aria-label="Back of business card">
    <svg class="facets" viewBox="0 0 500 305" width="500" height="305" aria-hidden="true">
      <polygon points="0,40 300,40 500,260 500,305 0,305" fill="var(--charcoal-light)"/>
      <polygon points="0,120 0,305 320,305 170,150" fill="var(--charcoal-dark)" opacity="0.45"/>
    </svg>
    <div class="wordmark">
      <span class="mark-square"></span><span class="name">Brenvale</span>
      <span class="legal">Constructions Pty Ltd</span>
    </div>
  </section>

  <section class="card card-front" aria-label="Front of business card">
    <div class="wordmark">
      <span class="mark-square"></span><span class="name">Brenvale</span>
      <span class="legal">Constructions Pty Ltd</span>
    </div>
    <div class="contact">
      <p class="person">Derek Lomavich</p>
      <p class="role">Managing Director</p>
      <p class="lines"><b>Mob:</b> 0438 215 706<br><b>Email:</b> derek@brenvale.com.au</p>
    </div>
    <p class="web">www.<span class="domain">brenvale</span>.com.au</p>
    <p class="registration">ACN: 381 607 912&nbsp;&nbsp;LIC: 617382D</p>
    <p class="services">Industrial • Commercial • Residential • Build Management</p>
  </section>
</body>
</html>
```